Velmoran Tabletop Deck Company (southern african focus for now) needs a e-commerce website

We need a website design for a playing card company based in Southern Africa/United States. We make locally-sourced playing cards (standard 52 card deck, with customized fronts and backs) for everyone and collaborate with local artists to uplift their talents, while celebrating their nation's culture, heritage, beauty and identity. We would like to see designs that use the colours blue (see flag of Eswatini as starting product), white and some red accents (or your recommendation). The final design should communicate elegance, fun and sustainable prosperity.

Target Market(s)

Everyone loves playing cards. From the solo adventurer to the party host, first time learner or expert, young, middle and old, we need to attract a broad audience that appreciates the finer things and supports sustainable, environmentally contentiousness causes that support the local economy and uplift local talent - thing global, act local.

Number of Pages Required

4 page

Font styles to use
Serif
Sans Serif

Requirements
Must have
• Pages to include Home (Main), About (Our Story), Shop and Contact
Nice to have
• While designs may be static, elements of graceful movement would be desirable. Perhaps functionality of scrolling down on homepage showing playing cards in use, front and back. Quindle and Zorbix store's capture that elegant yet rich look.
Should not have
• Too many products. We focus on 1-2.

```html
<!DOCTYPE html>
<html lang="en">
<head>
<meta charset="utf-8">
<title>Velmoran – Contact</title>
<link rel="stylesheet" href="https://fonts.googleapis.com/css2?family=Poppins:wght@400;500&family=Noto+Serif:wght@400&display=swap">
<style>
  :root{
    --navy:#24304a;
    --panel:#f3f3f3;
    --field:#ffffff;
    --ink:#111111;
    --body-text:#555555;
    --label:#8a8a8a;
    --footer-text:#e2e6ee;
    --accent-red:#d31212;
    --white:#ffffff;
  }
  *{box-sizing:border-box;margin:0;padding:0}
  html,body{width:1200px;height:836px;overflow:hidden}
  body{position:relative;background:var(--panel);font-family:"Poppins",sans-serif;color:var(--ink)}

  .site-header{position:absolute;left:0;top:0;width:1200px;height:104px;background:var(--navy)}
  .brand-name{position:absolute;font-family:"Noto Serif",serif;font-weight:400;color:var(--white);white-space:nowrap}
  .brand-mark{position:absolute;border:2px solid var(--white);border-radius:50%}
  .site-header .brand-mark{left:88px;top:38px;width:32px;height:32px}
  .site-header .brand-name{left:131px;top:39px;font-size:25px;line-height:30px}
  .main-nav a{position:absolute;top:45px;font-size:16px;line-height:22px;color:var(--white);text-decoration:none}
  .contact-button{position:absolute;left:993px;top:38px;width:119px;height:41px;background:var(--panel);color:var(--navy);font-size:16px;display:flex;align-items:center;justify-content:center;text-decoration:none}

  .intro-title{position:absolute;left:176px;top:180px;font-size:41px;font-weight:400;line-height:52px}
  .intro-text{position:absolute;left:176px;top:262px;width:290px;font-size:20.5px;line-height:31.6px;color:var(--body-text);white-space:nowrap}
  .social-heading{position:absolute;left:176px;top:461px;font-size:20.5px;font-weight:400;line-height:28px}
  .social-link{position:absolute;top:505px;width:41px;height:41px;border:2px solid var(--navy);border-radius:50%;display:flex;align-items:center;justify-content:center;font-size:8.5px;color:var(--navy);text-decoration:none}

  .field-label{position:absolute;left:522px;font-size:20.5px;color:var(--label);line-height:26px}
  .field-box{position:absolute;left:522px;width:503px;background:var(--field)}
  .send-button{position:absolute;left:522px;top:579px;width:153px;height:44px;border-radius:22px;background:var(--accent-red);color:var(--white);font-size:16px;font-weight:500;display:flex;align-items:center;justify-content:center;box-shadow:0 3px 6px rgba(0,0,0,.22)}

  .site-footer{position:absolute;left:0;top:679px;width:1200px;height:157px;background:var(--navy)}
  .site-footer .brand-mark{left:65px;top:40px;width:58px;height:58px}
  .site-footer .brand-name{left:142px;top:38px;font-size:48px;line-height:58px}
  .office-label,.office-detail{position:absolute;font-size:12.5px;line-height:16px;color:var(--footer-text)}
  .office-label{left:453px}
  .office-detail{left:622px}
  .office-icon{position:absolute;left:599px;width:15px;height:15px}
  .footer-social{position:absolute;top:36px;width:47px;height:47px;border:2px solid var(--white);border-radius:50%;display:flex;align-items:center;justify-content:center;font-size:9.5px;color:var(--white);text-decoration:none}
  .copyright{position:absolute;left:828px;top:96px;font-size:10px;color:var(--footer-text)}
</style>
</head>
<body>
  <header class="site-header">
    <span class="brand-mark"></span>
    <div class="brand-name">Velmoran</div>
    <nav class="main-nav">
      <a href="#" style="left:349px">Home</a>
      <a href="#" style="left:451px">About</a>
      <a href="#" style="left:555px">Shop</a>
      <a href="#" style="left:700px">Blog</a>
    </nav>
    <a href="#" class="contact-button">Contact</a>
  </header>

  <main>
    <h1 class="intro-title">Say Hello</h1>
    <p class="intro-text">Our tean will assess you<br>query and contact you<br>as soon as possible.<br>Simply fill out the form.</p>
    <h2 class="social-heading">Socialize with us</h2>
    <a href="#" class="social-link" style="left:176px">Folka</a>
    <a href="#" class="social-link" style="left:243px">Chirpo</a>
    <a href="#" class="social-link" style="left:310px">Linkra</a>
    <a href="#" class="social-link" style="left:377px">Snapla</a>

    <form class="contact-form">
      <label class="field-label" style="top:171px">Name</label>
      <div class="field-box" style="top:200px;height:43px"></div>
      <label class="field-label" style="top:280px">Email</label>
      <div class="field-box" style="top:309px;height:43px"></div>
      <label class="field-label" style="top:389px">Message</label>
      <div class="field-box" style="top:418px;height:127px"></div>
      <div class="send-button">Send</div>
    </form>
  </main>

  <footer class="site-footer">
    <span class="brand-mark"></span>
    <div class="brand-name">Velmoran</div>

    <span class="office-label" style="top:37px">Corporate office</span>
    <svg class="office-icon" style="top:38px" viewBox="0 0 16 16" fill="none" stroke="#e2e6ee" stroke-width="1.3"><path d="M4 2h2.5l1 3-1.5 1.2a8 8 0 0 0 3.8 3.8L11 8.5l3 1V12a2 2 0 0 1-2 2A10 10 0 0 1 2 4a2 2 0 0 1 2-2z"/></svg>
    <span class="office-detail" style="top:37px">+268 75550143</span>

    <span class="office-label" style="top:66px">International Branch</span>
    <svg class="office-icon" style="top:67px" viewBox="0 0 16 16" fill="none" stroke="#e2e6ee" stroke-width="1.3"><path d="M4 2h2.5l1 3-1.5 1.2a8 8 0 0 0 3.8 3.8L11 8.5l3 1V12a2 2 0 0 1-2 2A10 10 0 0 1 2 4a2 2 0 0 1 2-2z"/></svg>
    <span class="office-detail" style="top:66px">+268 75550143</span>

    <span class="office-label" style="top:95px">Contact Us</span>
    <svg class="office-icon" style="top:96px" viewBox="0 0 16 16" fill="none" stroke="#e2e6ee" stroke-width="1.3"><rect x="1" y="3" width="14" height="10" rx="1"/><path d="M1.5 3.5 8 9l6.5-5.5"/></svg>
    <span class="office-detail" style="top:95px">info@velmoran.com</span>

    <a href="#" class="footer-social" style="left:828px">Folka</a>
    <a href="#" class="footer-social" style="left:906px">Chirpo</a>
    <a href="#" class="footer-social" style="left:984px">Linkra</a>
    <a href="#" class="footer-social" style="left:1062px">Snapla</a>
    <p class="copyright">© All Rights Reserved. Velmoran. 2020</p>
  </footer>
</body>
</html>
```